Ecommerce brand for entrepreneurs needs help with branding products

I am looking for help to design a small supplement pouch. Including colours, layout and design.

The business:
The business is called 'Keel Orbit' and our goal is to help entrepreneurs continue to change the world in spite of how difficult it is.

At Keel Orbit, we understand being an entrepreneur is one of the hardest jobs there is. We believe there is a better way. A way in which you don’t have to choose between success in your business and the rest of your life. Our aim is to solve these challenges, so you can stay in the fight a little longer. If we can do this, we can ultimately change the world into a better place.

We will do this through a range of supplements, community, information and physical products to help you optimise their lives.

The product:
The product I am looking to create is for a natural nootropic called

‘The Velvet Compass’

The product will address the challenges with focus and lower attention spans.

So Entrepreneurs can Solve more problems, Help more people and make more money.

Do more in four hours than a whole day. Have Zen like calm. With Zero Jitters & Zero Crashes. Do what others can’t

The design:
I want this to be a small pouch. The final design should be elegant, and minimalist and have an edge that is different.

I have added examples of products that I like below.

I am open to most colour combinations but silver, navy, black, orange, white and translucent are what is taking my fancy right now.

I like the idea of having a translucent package or part of the package like some of the designs below. I also like the matt finish of some of the designs along with the flashes of shininess from silver for contrast. or even using embossing within the packaging.

I have a logo that I have made but I am open to changes on that as well if you see fit. if you do want to do this, I would love to see an emblem next to the words Keel Orbit that encapsulates the brand.

I have done some really really rough mockups myself but would like to see what you have to offer rather than what I have done

The purpose of this image:
I need a 3D mockup of this supplement to be on my landing page to start to take pre-orders.

I am ideally looking for 2 images

1) Supplement packaging on its own
2) Supplement packaging with background coloured lighting, with powder on the ground etc

Need extra days to review

Target Market(s)

The logo: Please also redesign my logo - I would love to see an emblem next to the words Keel Orbit that encapsulates the brand.The business is called 'Keel Orbit' and our goal is to help entrepreneurs continue to change the world in spite of how difficult it is. At Keel Orbit, we understand being an entrepreneur is one of the hardest jobs there is. We believe there is a better way. A way in which you don’t have to choose between success in your business and the rest of your life. Our aim is to solve these challenges, so you can stay in the fight a little longer. If we can do this, we can ultimately change the world into a better place. We will do this through a range of supplements, community, information and physical products to help you optimise their lives.

Industry/Entity Type

Supplements for entrepreneurs

Colors

Requirements
Must have
• The design: I want this to be a small pouch. The final design should be elegant, and minimalist and have an edge that is different. I have added examples of products that I like below. I am open to most colour combinations but silver, navy, black, orange, white and translucent are what is taking my fancy right now. I like the idea of having a translucent package or part of the package like some of the designs below. I also like the matt finish of some of the designs along with the flashes of shininess from silver for contrast. or even using embossing within the packaging.

```html
<!DOCTYPE html>
<html lang="en">
<head>
<meta charset="utf-8">
<title>Keel Orbit – The Velvet Compass pouch</title>
<link rel="stylesheet" href="https://fonts.googleapis.com/css2?family=Montserrat:wght@800;900&family=Cormorant+Garamond:wght@500&family=Oswald:wght@400;500&display=swap">
<style>
  :root {
    --navy: #1e2a4e;
    --navy-top: #2a3a59;
    --slate-teal: #4f6f79;
    --teal: #72bdb0;
    --white: #f4f4f2;
    --orange: #f08a24;
  }
  * { margin: 0; padding: 0; box-sizing: border-box; }
  html, body { width: 940px; height: 1200px; overflow: hidden; background: var(--navy); }
  .pouch-front {
    position: relative;
    width: 940px;
    height: 1200px;
    background: var(--navy);
    color: var(--white);
  }
  .label-top {
    position: absolute;
    inset: 0 0 420px 0;
    background: linear-gradient(180deg, var(--navy-top) 0%, var(--slate-teal) 45%, var(--teal) 100%);
  }
  .brand-top {
    position: absolute;
    top: 190px;
    left: 0; right: 0;
    text-align: center;
    font-family: "Montserrat", sans-serif;
    font-weight: 800;
    font-size: 30px;
    letter-spacing: 2px;
    color: var(--white);
  }
  .title-frame {
    position: absolute;
    top: 290px;
    left: 135px;
    width: 670px;
    height: 400px;
    border: 9px solid var(--white);
    padding: 12px;
    display: flex;
    flex-direction: column;
    font-family: "Montserrat", sans-serif;
    font-weight: 900;
  }
  .title-band {
    flex: 1;
    display: flex;
    align-items: center;
    padding: 0 44px;
  }
  .band-the { background: var(--slate-teal); justify-content: space-between; font-size: 64px; color: var(--white); }
  .band-velvet { background: var(--white); justify-content: space-between; font-size: 64px; color: var(--slate-teal); }
  .band-compass { background: var(--teal); justify-content: center; font-size: 80px; color: var(--white); letter-spacing: -1px; }
  .tagline {
    position: absolute;
    top: 850px;
    left: 0; right: 0;
    text-align: center;
    font-family: "Cormorant Garamond", serif;
    font-weight: 500;
  }
  .tagline-main { font-size: 66px; line-height: 1; }
  .tagline-sub { font-size: 38px; margin-top: 8px; }
  .product-info {
    position: absolute;
    left: 150px;
    top: 1050px;
    font-family: "Oswald", sans-serif;
    font-weight: 500;
    font-size: 25px;
    line-height: 1.4;
    text-transform: uppercase;
  }
  .product-info .flavour-name { color: var(--orange); }
  .product-info .net-weight { text-transform: none; font-weight: 400; }
  .product-info .net-weight b { font-weight: 500; }
  .brand-bottom {
    position: absolute;
    right: 130px;
    top: 1112px;
    font-family: "Montserrat", sans-serif;
    font-weight: 800;
    font-size: 32px;
    letter-spacing: 1px;
  }
</style>
</head>
<body>
  <main class="pouch-front">
    <div class="label-top"></div>
    <div class="brand-top">Keel Orbit</div>

    <div class="title-frame">
      <div class="title-band band-the"><span>T</span><span>H</span><span>E</span></div>
      <div class="title-band band-velvet"><span>V</span><span>E</span><span>L</span><span>V</span><span>E</span><span>T</span></div>
      <div class="title-band band-compass">COMPASS</div>
    </div>

    <div class="tagline">
      <p class="tagline-main">Flow - Clarity - Drive</p>
      <p class="tagline-sub">For Founders &amp; Entrepreneurs</p>
    </div>

    <div class="product-info">
      <p>A Natural Nootropic</p>
      <p><span class="flavour-name">Orange &amp; Mango</span> Flavour</p>
      <p class="net-weight"><b>240g</b> (30 Servings)</p>
    </div>

    <div class="brand-bottom">Keel Orbit</div>
  </main>
</body>
</html>
```